Moodvane - Landing Page

Need a landing page for a journal app. The app is based on a retrospective board, where each journal entry is split into 3 sections: "What went well", "What Didn't Go Well" and "Things To Try".
The landing page should match the style of all modern web application landing pages. Think Plumo, Vexora, Zenquil. I've included screenshots of the app.
One feature that I want to highlight that is not ready yet, is an AI coach. It will offer insights based on the history of the user's journal entries
1 page

```html
<!DOCTYPE html>
<html lang="en">
<head>
<meta charset="utf-8">
<title>Moodvane – Your Daily Journal</title>
<link href="https://fonts.googleapis.com/css2?family=Poppins:wght@400;500;600;700&family=Montserrat:wght@300;400;500;600;700&display=swap" rel="stylesheet">
<style>
:root{
  --blue:#0a4da6;
  --blue-deep:#083f8f;
  --blue-bright:#1562c4;
  --blue-soft:#c9dcf2;
  --blue-pale:#e6eef7;
  --navy:#1c2b5c;
  --ink:#111827;
  --text:#3a3f4a;
  --muted:#7a808c;
  --page:#fbfaf7;
  --white:#ffffff;
  --panel:#dbe4ee;
  --line:#d9dde4;
}
*{box-sizing:border-box;margin:0;padding:0}
html,body{width:1200px;height:4934px;overflow:hidden}
body{position:relative;background:var(--page);font-family:"Montserrat",sans-serif;color:var(--text)}
.abs{position:absolute}
.heading{font-family:"Poppins",sans-serif;font-weight:700;color:var(--ink);font-size:38px;line-height:46px;text-align:center}
.heading .accent{color:var(--blue)}
.eyebrow{font-family:"Montserrat",sans-serif;font-size:21px;color:var(--ink);text-align:center}
.btn{position:absolute;display:flex;align-items:center;justify-content:center;font-family:"Poppins",sans-serif;font-weight:600;font-size:13px;border-radius:3px}
.btn-solid{background:var(--blue);color:var(--white)}
.btn-soft{background:var(--blue-soft);color:var(--blue)}
.btn-line{border:1.5px solid var(--white);color:var(--white)}

/* hero */
.hero{left:0;top:0;width:1200px;height:652px;background:linear-gradient(120deg,#0a4aa3 0%,#0b54b5 45%,#0a4ba7 70%,#0d58bb 100%);overflow:hidden}
.hero-stripe{position:absolute;width:260px;height:900px;background:rgba(255,255,255,.05);transform:rotate(35deg)}
.logo{font-family:"Poppins",sans-serif;font-weight:700;font-size:33px;color:var(--white);letter-spacing:-.3px}
.nav a{position:absolute;top:31px;font-size:13px;color:var(--white);text-decoration:none}
.hero-eyebrow{left:0;top:136px;width:1200px;text-align:center;color:var(--white);font-size:22px}
.hero-title{left:0;top:176px;width:1200px;color:var(--white);font-size:38px;line-height:46px}

/* app window */
.app{left:140px;top:402px;width:920px;height:568px;background:#f0f3f7;border-radius:8px;box-shadow:0 10px 30px rgba(20,40,80,.15);overflow:hidden}
.app-bar{left:0;top:0;width:920px;height:60px;background:var(--white)}
.app-logo{left:34px;top:12px;font-family:"Poppins",sans-serif;font-weight:700;font-size:25px;color:var(--blue)}
.app-search{left:496px;top:21px;width:211px;height:24px;border:1.5px solid #9fb6d6;border-radius:3px;font-size:8px;color:var(--muted);padding:6px 10px}
.avatar{background:linear-gradient(160deg,#c9b5a3,#6b5a4f);border-radius:3px}
.app-user{left:770px;top:22px;font-size:8px;font-weight:600;color:var(--ink);line-height:11px}
.app-user span{display:block;font-weight:400;color:var(--muted);font-size:7px}
.app-nav{left:0;top:60px;width:46px;height:508px;background:var(--navy)}
.app-menu{left:46px;top:60px;width:105px;height:508px;background:#cfe0f3}
.menu-item{position:absolute;left:10px;font-size:9.5px;font-weight:600;color:var(--ink);white-space:nowrap}
.menu-active{left:0;top:40px;width:113px;height:27px;background:#7fa6d8;border-radius:0 4px 4px 0;color:var(--white);font-size:9.5px;font-weight:600;padding:8px 10px;white-space:nowrap}
.app-entry{left:216px;top:83px;font-family:"Poppins",sans-serif;font-weight:600;font-size:14px;color:var(--ink)}
.app-date{left:216px;top:103px;font-size:9px;font-weight:700;color:var(--ink)}
.gym-pill{background:#8fb2dd;color:var(--white);border-radius:2px;display:flex;align-items:center;justify-content:center}
.app-card{left:178px;top:131px;width:587px;height:400px;background:var(--white);border-radius:8px;box-shadow:0 3px 14px rgba(20,40,80,.08)}
.entry-row{position:absolute;display:flex;gap:12px;align-items:flex-start;font-size:13px;font-weight:500;color:var(--ink);line-height:15px}
.app-input{left:38px;top:335px;width:510px;height:35px;background:#f5f7fa;border-radius:4px;font-size:10px;color:var(--ink);padding:12px 24px}
.app-tools{left:792px;top:60px;width:128px;height:508px;background:#ececec}
.tool-select{left:9px;top:17px;width:109px;height:23px;background:var(--white);border:1px solid var(--line);border-radius:3px;font-size:8px;padding:6px}
.tool-row{position:absolute;left:12px;display:flex;gap:18px;font-size:12px;font-weight:700;color:var(--ink)}
.tool-sep{position:absolute;left:0;width:128px;height:1px;background:#d6d6d6}

/* steps */
.step-icon{width:50px;height:50px;border-radius:6px;background:var(--blue);display:flex;align-items:center;justify-content:center}
.step-title{font-family:"Montserrat",sans-serif;font-size:38px;font-weight:400;color:var(--ink)}
.step-text{width:430px;font-size:14.5px;line-height:22px;color:var(--text)}
.step-text p+p{margin-top:7px}
.step-text strong{color:var(--blue);font-weight:600}

/* mini app */
.mini{position:absolute;width:464px;height:320px}
.mini-back{left:23px;top:0;width:385px;height:320px;background:var(--panel);border-radius:10px;box-shadow:0 12px 30px rgba(20,40,80,.12)}
.mini-side{left:0;top:60px;width:42px;height:220px;background:var(--white);border-radius:6px;box-shadow:0 4px 14px rgba(20,40,80,.12)}
.mini-ico{position:absolute;left:13px;width:16px;height:16px;border-radius:3px;display:flex;align-items:center;justify-content:center}
.mini-ico.on{background:var(--blue)}
.mini-card{left:79px;top:60px;width:262px;height:220px;background:var(--white);border-radius:6px;box-shadow:0 4px 14px rgba(20,40,80,.1)}
.mini-tools{left:366px;top:56px;width:94px;height:224px;background:var(--white);border-radius:6px;box-shadow:0 4px 14px rgba(20,40,80,.12)}
.mini-row{position:absolute;left:20px;width:225px;display:flex;gap:8px;font-size:7px;line-height:9px;font-weight:500;color:var(--ink)}
.mini-row .avatar{flex:none;width:18px;height:18px}
.mini-bar{left:16px;bottom:14px;width:230px;height:16px;background:#f3f5f8;border-radius:3px;font-size:5px;padding:5px 10px;color:var(--ink);white-space:nowrap;overflow:hidden}

/* why */
.why{left:0;top:2789px;width:1200px;height:591px;background:linear-gradient(120deg,#0a4aa3,#0b52b2 60%,#0a4ba7)}
.why .eyebrow,.why .heading{color:var(--white)}
.feature{position:absolute;top:234px;width:288px;height:207px;background:var(--white);border-radius:5px}
.feature h3{position:absolute;left:21px;top:103px;font-size:21px;font-weight:500;color:var(--ink)}
.feature p{position:absolute;left:21px;top:139px;width:200px;font-size:10.5px;line-height:14px;color:var(--muted)}
.feature .go{position:absolute;right:13px;top:159px;width:34px;height:34px;border-radius:50%;background:var(--blue-soft);display:flex;align-items:center;justify-content:center}
.feature svg.fi{position:absolute;left:21px;top:30px}

/* testimonials */
.quote-card{left:84px;top:3652px;width:976px;height:450px;background:var(--blue-pale);border-radius:6px;overflow:hidden;border:1px solid #dfe6ef}
.quote-photo{left:0;top:0;width:359px;height:450px;background:linear-gradient(135deg,#7d8a7c 0%,#4c5245 45%,#2a2b28 100%)}
.quote-text{left:470px;top:117px;width:450px;font-size:19px;line-height:31px;color:var(--ink)}
.next-card{left:1118px;top:3652px;width:120px;height:450px;background:linear-gradient(135deg,#b9b0a8,#8f8780);border-radius:6px}
.round{position:absolute;width:50px;height:50px;border-radius:50%;display:flex;align-items:center;justify-content:center}

/* cta */
.cta{left:0;top:4214px;width:1200px;height:362px;background:linear-gradient(120deg,#0a4aa3,#0b53b4 55%,#0a4ba7)}
.cta .eyebrow,.cta .heading{color:var(--white)}

/* footer */
.footer{left:0;top:4576px;width:1200px;height:358px;background:#f2f4f7}
.footer h4{position:absolute;font-size:12px;font-weight:700;color:var(--blue)}
.footer ul{position:absolute;list-style:none;font-size:11.5px;line-height:23px;color:var(--text)}
.social{position:absolute;top:142px;width:26px;height:26px;background:var(--white);border:1px solid var(--line);border-radius:3px}
.contact-line{position:absolute;left:757px;display:flex;gap:8px;font-size:11px;line-height:17px;color:var(--text)}
.footer .copy{position:absolute;left:0;top:331px;width:1200px;text-align:center;font-size:10.5px;color:var(--text)}
</style>
</head>
<body>

<!-- HERO -->
<section class="abs hero">
  <div class="hero-stripe" style="left:-80px;top:-150px"></div>
  <div class="hero-stripe" style="left:900px;top:-250px"></div>
  <div class="hero-stripe" style="left:1050px;top:-100px;width:120px"></div>
  <div class="abs logo" style="left:140px;top:16px">Moodvane</div>
  <nav class="nav">
    <a style="left:464px">Home</a><a style="left:525px">About</a><a style="left:587px">Features</a><a style="left:663px">How It Works</a><a style="left:772px">Contact</a>
  </nav>
  <div class="btn btn-line" style="left:845px;top:27px;width:94px;height:31px">Login</div>
  <div class="btn btn-soft" style="left:947px;top:27px;width:111px;height:31px">Sign Up</div>
  <div class="abs hero-eyebrow">Reflect, Grow, Succeed.</div>
  <h1 class="abs heading hero-title">Your Daily Journal For Thoughtful<br>Retrospectives.</h1>
  <div class="btn btn-soft" style="left:512px;top:300px;width:174px;height:41px;font-size:14px">Start Your Journey</div>
</section>

<!-- APP WINDOW -->
<div class="abs app">
  <div class="abs app-bar"></div>
  <div class="abs app-logo">Moodvane</div>
  <div class="abs app-search">search
    <svg style="position:absolute;right:6px;top:5px" width="11" height="11" viewBox="0 0 12 12"><circle cx="5" cy="5" r="3.6" fill="none" stroke="#1c2b5c" stroke-width="1.5"/><path d="M8 8l3 3" stroke="#1c2b5c" stroke-width="1.5"/></svg>
  </div>
  <div class="abs avatar" role="img" aria-label="User profile photo" style="left:715px;top:20px;width:22px;height:22px"></div>
  <div class="abs app-user" style="left:743px">Darin Okafor<span>gym trainer</span></div>

  <div class="abs app-nav">
    <svg class="abs" style="left:13px;top:50px" width="20" height="24" viewBox="0 0 20 24"><rect x="0" y="0" width="20" height="24" rx="3" fill="#3c4c7c"/><rect x="5" y="4" width="10" height="14" rx="1" fill="#fff"/><path d="M7 8h6M7 11h6M7 14h4" stroke="#1c2b5c"/></svg>
    <svg class="abs" style="left:15px;top:104px" width="16" height="16" viewBox="0 0 16 16"><rect x="1" y="3" width="14" height="12" rx="1" fill="#fff"/><path d="M3 7h10M3 10h10M6 7v6M10 7v6" stroke="#1c2b5c"/></svg>
    <svg class="abs" style="left:16px;top:148px" width="14" height="17" viewBox="0 0 14 17"><rect x="1" y="1" width="12" height="15" rx="1" fill="#fff"/><path d="M3 11h8" stroke="#1c2b5c"/></svg>
    <svg class="abs" style="left:15px;top:193px" width="16" height="16" viewBox="0 0 16 16"><circle cx="8" cy="8" r="7" fill="none" stroke="#fff" stroke-width="1.4"/><circle cx="8" cy="6.5" r="2.3" fill="#fff"/><path d="M4 13c1-2 7-2 8 0" stroke="#fff" stroke-width="1.4" fill="none"/></svg>
    <div class="abs" style="left:19px;top:387px;width:7px;height:7px;border-radius:50%;background:#fff"></div>
    <div class="abs" style="left:19px;top:407px;width:7px;height:7px;border-radius:50%;background:#fff"></div>
    <div class="abs" style="left:19px;top:427px;width:7px;height:7px;border-radius:50%;background:#fff"></div>
    <div class="abs" style="left:19px;top:447px;width:7px;height:7px;border-radius:50%;background:#7fa6d8"></div>
  </div>
  <div class="abs app-menu">
    <div class="abs menu-active">What Went Well</div>
    <div class="menu-item" style="top:98px">What Didn't Go Well</div>
    <div class="menu-item" style="top:132px">Things To Try.</div>
    <div class="menu-item" style="top:460px;font-size:8px;display:flex;gap:4px;align-items:center;left:24px">
      <svg width="11" height="10" viewBox="0 0 11 10"><path d="M6 1H1v8h5M4 5h6M8 3l2 2-2 2" fill="none" stroke="#1c2b5c"/></svg>Sign out</div>
  </div>

  <div class="abs app-entry">Entry</div>
  <div class="abs app-date">
    <svg width="9" height="9" viewBox="0 0 9 9" style="vertical-align:-1px"><rect x=".5" y="1" width="8" height="7.5" fill="#1c2b5c"/></svg> Thu Aug 22 2024</div>
  <div class="abs gym-pill" style="left:644px;top:85px;width:73px;height:19px;font-size:10px">Gym</div>

  <div class="abs app-card">
    <div class="entry-row" style="left:31px;top:46px">
      <div class="avatar" role="img" aria-label="Portrait photo of a team member" style="width:40px;height:40px;flex:none"></div>
      <div style="padding-top:10px">Completed all scheduled workouts<br>this week</div>
    </div>
    <div class="entry-row" style="left:31px;top:144px">
      <div class="avatar" role="img" aria-label="Portrait photo of a team member" style="width:40px;height:40px;flex:none;background:linear-gradient(160deg,#9a8f86,#3b3a3a)"></div>
      <div style="padding-top:10px">Increased bench press weight by 10<br>pounds.</div>
    </div>
    <div class="abs app-input">Maintained consistent energy levels throughout sessions.
      <svg style="position:absolute;right:52px;top:10px" width="18" height="16" viewBox="0 0 18 16"><path d="M1 8l16-7-5 14-3-6z" fill="none" stroke="#1c2b5c" stroke-width="1.4"/></svg>
      <svg style="position:absolute;right:14px;top:12px" width="8" height="11" viewBox="0 0 8 11"><path d="M1 1l5 4.5L1 10" fill="none" stroke="#1c2b5c" stroke-width="1.5"/></svg>
    </div>
  </div>

  <div class="abs app-tools">
    <div class="abs tool-select">Font
      <svg style="position:absolute;right:6px;top:8px" width="8" height="5" viewBox="0 0 8 5"><path d="M1 1l3 3 3-3" fill="none" stroke="#333"/></svg></div>
    <div class="tool-sep" style="top:58px"></div>
    <div class="tool-row" style="top:79px;gap:22px"><span>B</span><span style="font-style:italic;font-weight:400">I</span><span style="text-decoration:underline;font-weight:400">U</span><span style="text-decoration:line-through;font-weight:400">S</span></div>
    <div class="tool-sep" style="top:113px"></div>
    <div class="tool-row" style="top:136px;gap:14px">
      <svg width="18" height="12" viewBox="0 0 18 12"><path d="M5 2h13M5 6h13M5 10h13M1 2h2M1 6h2M1 10h2" stroke="#333"/></svg>
      <svg width="18" height="12" viewBox="0 0 18 12"><path d="M5 2h13M5 6h13M5 10h13M1 1v3M1 5v3M1 9v3" stroke="#333"/></svg>
      <svg width="18" height="12" viewBox="0 0 18 12"><path d="M6 2h12M6 6h12M6 10h12M0 4l3 2-3 2" stroke="#333" fill="none"/></svg>
      <svg width="18" height="12" viewBox="0 0 18 12"><path d="M6 2h12M6 6h12M6 10h12M3 4L0 6l3 2" stroke="#333" fill="none"/></svg>
    </div>
    <div class="tool-sep" style="top:166px"></div>
    <div class="tool-row" style="top:186px;font-size:20px;font-family:Georgia,serif;gap:20px"><span>&#8220;</span><span style="font-size:13px;font-family:Montserrat,sans-serif;padding-top:4px">T<sub style="font-size:7px">x</sub></span></div>
  </div>
</div>

<!-- HOW IT WORKS -->
<div class="abs eyebrow" style="left:0;top:1078px;width:1200px">How Moodvane Works</div>
<h2 class="abs heading" style="left:0;top:1115px;width:1200px">The Moodvane Method Simple<br>Steps to <span class="accent">Growth</span></h2>

<svg class="abs" style="left:0;top:0" width="1200" height="4934" aria-hidden="true">
  <path d="M673 1590V1660Q673 1682 651 1682H551Q529 1682 529 1704V1758" fill="none" stroke="#2a63b8" stroke-width="1.3" stroke-dasharray="3 3"/>
  <circle cx="673" cy="1590" r="3" fill="#2a63b8"/><circle cx="529" cy="1758" r="3" fill="#2a63b8"/>
  <path d="M525 2128V2202Q525 2224 547 2224H683Q705 2224 705 2246V2291" fill="none" stroke="#2a63b8" stroke-width="1.3" stroke-dasharray="3 3"/>
  <circle cx="525" cy="2128" r="3" fill="#2a63b8"/><circle cx="705" cy="2291" r="3" fill="#2a63b8"/>
</svg>

<!-- Step 1 -->
<div class="abs step-icon" style="left:142px;top:1238px">
  <svg width="24" height="22" viewBox="0 0 24 22"><rect x="1" y="9" width="5" height="12" rx="1" fill="#fff"/><path d="M8 10l5-8c2 0 3 1 2.5 3.5L15 9h6c1.5 0 2.5 1.4 2 2.8l-2.5 8C20 21 19 21 18 21H8z" fill="#fff"/></svg>
</div>
<div class="abs step-title" style="left:140px;top:1306px">What Went Well</div>
<div class="abs step-text" style="left:140px;top:1367px">
  <p>Start each entry by noting the wins of your day, big or small. Capturing what went well builds momentum, reminds you of progress you might overlook, and keeps a clear record of the habits that are truly working for you.</p>
  <p>Add a tag to any note, group entries by area of life, and look back on a growing list of wins whenever you need a boost.</p>
</div>
<div class="btn btn-solid" style="left:140px;top:1578px;width:174px;height:42px">Try Moodvane Now</div>

<div class="mini" style="left:652px;top:1256px">
  <div class="abs mini-back">
    <div class="abs" style="left:18px;top:16px;width:5px;height:5px;border-radius:50%;background:#2a63b8"></div>
    <div class="abs" style="left:27px;top:16px;width:5px;height:5px;border-radius:50%;background:#2a63b8"></div>
    <div class="abs avatar" role="img" aria-label="User profile photo" style="left:290px;top:10px;width:15px;height:15px"></div>
    <div class="abs" style="left:309px;top:11px;font-size:6px;font-weight:600;color:#111;line-height:7px">Darin Okafor<br><span style="font-weight:400;color:#777">gym trainer</span></div>
  </div>
  <div class="abs mini-side">
    <div class="mini-ico on" style="top:14px"><svg width="9" height="9" viewBox="0 0 24 22"><path d="M1 9h5v12H1zM8 10l5-8c2 0 3 1 2.5 3.5L15 9h6c1.5 0 2.5 1.4 2 2.8l-2.5 8C20 21 19 21 18 21H8z" fill="#fff"/></svg></div>
    <div class="mini-ico" style="top:40px"><svg width="9" height="9" viewBox="0 0 10 10"><path d="M5 1l4 8H1z" fill="#555"/></svg></div>
    <div class="mini-ico" style="top:64px"><svg width="8" height="9" viewBox="0 0 8 10"><path d="M2 0h4v3l2 7H0l2-7z" fill="#555"/></svg></div>
    <div class="mini-ico" style="top:190px"><svg width="9" height="8" viewBox="0 0 11 10"><path d="M6 1H1v8h5M4 5h6" fill="none" stroke="#555"/></svg></div>
  </div>
  <div class="abs mini-card">
    <div class="abs" style="left:20px;top:14px;font-size:8px;font-weight:700;color:#111">Entry</div>
    <div class="abs" style="left:20px;top:24px;font-size:5.5px;font-weight:700;color:#111">&#9632; Thu Aug 22 2024</div>
    <div class="abs gym-pill" style="left:196px;top:14px;width:46px;height:10px;font-size:6px">Gym</div>
    <div class="mini-row" style="top:58px"><div class="avatar" role="img" aria-label="Portrait photo of a team member"></div><div style="padding-top:4px">Completed all scheduled workouts this week</div></div>
    <div class="mini-row" style="top:110px"><div class="avatar" role="img" aria-label="Portrait photo of a team member" style="background:linear-gradient(160deg,#9a8f86,#3b3a3a)"></div><div>Increased bench press weight by 10<br>pounds.</div></div>
    <div class="abs mini-bar">Maintained consistent energy levels throughout sessions.</div>
  </div>
  <div class="abs mini-tools">
    <div class="abs" style="left:8px;top:10px;width:78px;height:12px;border:1px solid #ddd;border-radius:2px;font-size:5px;padding:3px">Font</div>
    <div class="abs" style="left:10px;top:40px;font-size:7px;font-weight:700;color:#111;word-spacing:10px">B <i>I</i> <u>U</u> <s>S</s></div>
    <div class="abs" style="left:10px;top:68px;font-size:8px;color:#555;letter-spacing:6px">&#8801;&#8801;&#8801;&#8801;</div>
    <div class="abs" style="left:10px;top:88px;font-size:14px;font-family:Georgia,serif;font-weight:700;color:#111">&#8220; <span style="font-size:8px;font-family:Montserrat,sans-serif;font-weight:400">T</span></div>
  </div>
</div>

<!-- Step 2 -->
<div class="mini" style="left:117px;top:1792px">
  <div class="abs mini-back">
    <div class="abs" style="left:18px;top:16px;width:5px;height:5px;border-radius:50%;background:#2a63b8"></div>
    <div class="abs" style="left:27px;top:16px;width:5px;height:5px;border-radius:50%;background:#2a63b8"></div>
    <div class="abs avatar" role="img" aria-label="User profile photo" style="left:290px;top:10px;width:15px;height:15px"></div>
    <div class="abs" style="left:309px;top:11px;font-size:6px;font-weight:600;color:#111;line-height:7px">Darin Okafor<br><span style="font-weight:400;color:#777">gym trainer</span></div>
  </div>
  <div class="abs mini-side">
    <div class="mini-ico" style="top:14px"><svg width="9" height="9" viewBox="0 0 24 22"><path d="M1 9h5v12H1zM8 10l5-8c2 0 3 1 2.5 3.5L15 9h6c1.5 0 2.5 1.4 2 2.8l-2.5 8C20 21 19 21 18 21H8z" fill="#555"/></svg></div>
    <div class="mini-ico on" style="top:40px"><svg width="9" height="9" viewBox="0 0 10 10"><path d="M5 1l4 8H1z" fill="#fff"/></svg></div>
    <div class="mini-ico" style="top:64px"><svg width="8" height="9" viewBox="0 0 8 10"><path d="M2 0h4v3l2 7H0l2-7z" fill="#555"/></svg></div>
    <div class="mini-ico" style="top:190px"><svg width="9" height="8" viewBox="0 0 11 10"><path d="M6 1H1v8h5M4 5h6" fill="none" stroke="#555"/></svg></div>
  </div>
  <div class="abs mini-card">
    <div class="abs" style="left:20px;top:14px;font-size:8px;font-weight:700;color:#111">Entry</div>
    <div class="abs" style="left:20px;top:24px;font-size:5.5px;font-weight:700;color:#111">&#9632; Thu Aug 22 2024</div>
    <div class="abs gym-pill" style="left:196px;top:14px;width:46px;height:10px;font-size:6px">Gym</div>
    <div class="mini-row" style="top:58px"><div class="avatar" role="img" aria-label="Portrait photo of a team member"></div><div>Struggled with form on deadlifts, leading to<br>lower back discomfort.</div></div>
    <div class="mini-row" style="top:110px"><div class="avatar" role="img" aria-label="Portrait photo of a team member" style="background:linear-gradient(160deg,#9a8f86,#3b3a3a)"></div><div>Skipped meal prep, resulting in inconsistent<br>nutrition.</div></div>
    <div class="abs mini-bar">Missed two morning sessions after late nights.</div>
  </div>
  <div class="abs mini-tools">
    <div class="abs" style="left:8px;top:10px;width:78px;height:12px;border:1px solid #ddd;border-radius:2px;font-size:5px;padding:3px">Font</div>
    <div class="abs" style="left:10px;top:40px;font-size:7px;font-weight:700;color:#111;word-spacing:10px">B <i>I</i> <u>U</u> <s>S</s></div>
    <div class="abs" style="left:10px;top:68px;font-size:8px;color:#555;letter-spacing:6px">&#8801;&#8801;&#8801;&#8801;</div>
    <div class="abs" style="left:10px;top:88px;font-size:14px;font-family:Georgia,serif;font-weight:700;color:#111">&#8220; <span style="font-size:8px;font-family:Montserrat,sans-serif;font-weight:400">T</span></div>
  </div>
</div>

<div class="abs step-icon" style="left:638px;top:1744px">
  <svg width="24" height="22" viewBox="0 0 24 22"><path d="M12 1l11 20H1z" fill="#fff"/><path d="M12 8v6" stroke="#0a4da6" stroke-width="2.4"/><circle cx="12" cy="17.5" r="1.3" fill="#0a4da6"/></svg>
</div>
<div class="abs step-title" style="left:638px;top:1812px">What Didn't Go Well?</div>
<div class="abs step-text" style="left:638px;top:1874px">
  <p>Be honest about what held you back. Naming setbacks, missed goals and tough moments without judgment turns them into lessons, and helps you spot the patterns that keep showing up in your week.</p>
  <p>Keep it short and kind. A few clear lines are enough to understand what went wrong and set the stage for a better plan tomorrow.</p>
</div>
<div class="btn btn-solid" style="left:638px;top:2086px;width:175px;height:41px">Try Moodvane Now</div>

<!-- Step 3 -->
<div class="abs step-icon" style="left:142px;top:2287px">
  <svg width="20" height="24" viewBox="0 0 20 24"><path d="M6 1h8M7.5 1v7L1 21c-.5 1 .2 2 1.2 2h15.6c1 0 1.7-1 1.2-2L12.5 8V1" fill="#fff" stroke="#fff" stroke-width="1.5"/><path d="M4 16h12" stroke="#0a4da6" stroke-width="1.5"/></svg>
</div>
<div class="abs step-title" style="left:142px;top:2355px">Things To Try</div>
<div class="abs step-text" style="left:140px;top:2417px">
  <p>Turn reflection into action by listing small experiments for the days ahead. Each idea is easy to track, so you can see which changes stick and which ones need another try next week.</p>
  <p><strong>Coming soon: AI Coach.</strong> It reads the history of your journal entries and offers personal insights and fresh things to try, based on your own patterns.</p>
</div>
<div class="btn btn-solid" style="left:142px;top:2626px;width:174px;height:42px">Try Moodvane Now</div>

<div class="mini" style="left:652px;top:2300px">
  <div class="abs mini-back">
    <div class="abs" style="left:18px;top:16px;width:5px;height:5px;border-radius:50%;background:#2a63b8"></div>
    <div class="abs" style="left:27px;top:16px;width:5px;height:5px;border-radius:50%;background:#2a63b8"></div>
    <div class="abs avatar" role="img" aria-label="User profile photo" style="left:290px;top:10px;width:15px;height:15px"></div>
    <div class="abs" style="left:309px;top:11px;font-size:6px;font-weight:600;color:#111;line-height:7px">Darin Okafor<br><span style="font-weight:400;color:#777">gym trainer</span></div>
  </div>
  <div class="abs mini-side">
    <div class="mini-ico" style="top:14px"><svg width="9" height="9" viewBox="0 0 24 22"><path d="M1 9h5v12H1zM8 10l5-8c2 0 3 1 2.5 3.5L15 9h6c1.5 0 2.5 1.4 2 2.8l-2.5 8C20 21 19 21 18 21H8z" fill="#555"/></svg></div>
    <div class="mini-ico" style="top:40px"><svg width="9" height="9" viewBox="0 0 10 10"><path d="M5 1l4 8H1z" fill="#555"/></svg></div>
    <div class="mini-ico on" style="top:64px"><svg width="8" height="9" viewBox="0 0 8 10"><path d="M2 0h4v3l2 7H0l2-7z" fill="#fff"/></svg></div>
    <div class="mini-ico" style="top:190px"><svg width="9" height="8" viewBox="0 0 11 10"><path d="M6 1H1v8h5M4 5h6" fill="none" stroke="#555"/></svg></div>
  </div>
  <div class="abs mini-card">
    <div class="abs" style="left:20px;top:14px;font-size:8px;font-weight:700;color:#111">Entry</div>
    <div class="abs" style="left:20px;top:24px;font-size:5.5px;font-weight:700;color:#111">&#9632; Thu Aug 22 2024</div>
    <div class="abs gym-pill" style="left:196px;top:14px;width:46px;height:10px;font-size:6px">Gym</div>
    <div class="mini-row" style="top:58px"><div class="avatar" role="img" aria-label="Portrait photo of a team member"></div><div>Focus on deadlift form by lowering the weight<br>and reviewing proper technique.</div></div>
    <div class="mini-row" style="top:110px"><div class="avatar" role="img" aria-label="Portrait photo of a team member" style="background:linear-gradient(160deg,#9a8f86,#3b3a3a)"></div><div>Set reminders for post-workout stretching<br>to prevent muscle tightness.</div></div>
    <div class="abs mini-bar">Schedule a full recovery day in the middle of the week.</div>
  </div>
  <div class="abs mini-tools">
    <div class="abs" style="left:8px;top:10px;width:78px;height:12px;border:1px solid #ddd;border-radius:2px;font-size:5px;padding:3px">Font</div>
    <div class="abs" style="left:10px;top:40px;font-size:7px;font-weight:700;color:#111;word-spacing:10px">B <i>I</i> <u>U</u> <s>S</s></div>
    <div class="abs" style="left:10px;top:68px;font-size:8px;color:#555;letter-spacing:6px">&#8801;&#8801;&#8801;&#8801;</div>
    <div class="abs" style="left:10px;top:88px;font-size:14px;font-family:Georgia,serif;font-weight:700;color:#111">&#8220; <span style="font-size:8px;font-family:Montserrat,sans-serif;font-weight:400">T</span></div>
  </div>
</div>

<!-- WHY -->
<section class="abs why">
  <div class="abs eyebrow" style="left:0;top:71px;width:1200px">Why Moodvane?</div>
  <h2 class="abs heading" style="left:0;top:108px;width:1200px">Discover the Power of<br>Moodvane</h2>

  <div class="feature" style="left:140px">
    <svg class="fi" width="54" height="56" viewBox="0 0 54 56"><path d="M24 10c-10 0-17 7-17 16 0 5 2 8 5 11v15h18v-7h7c2 0 3-1 3-3v-6l5-2-5-8c0-9-7-16-16-16z" fill="#0a4da6"/><circle cx="24" cy="26" r="7" fill="#fff"/><circle cx="24" cy="26" r="3" fill="#0a4da6"/><path d="M24 1v5M10 5l3 4M38 5l-3 4M4 14l4 2M44 14l-4 2" stroke="#0a4da6" stroke-width="2.2" stroke-linecap="round"/></svg>
    <h3>Mental Clarity</h3>
    <p>Regular reflection helps clear your mind and stay focused.</p>
    <div class="go"><svg width="13" height="13" viewBox="0 0 13 13"><path d="M2 11L11 2M4 2h7v7" fill="none" stroke="#0a4da6" stroke-width="2"/></svg></div>
  </div>
  <div class="feature" style="left:456px">
    <svg class="fi" width="70" height="54" viewBox="0 0 70 54"><circle cx="14" cy="18" r="7" fill="#0a4da6"/><path d="M1 50c0-12 6-20 13-20s13 8 13 20z" fill="#0a4da6"/><circle cx="33" cy="24" r="6" fill="#0a4da6"/><path d="M22 52c0-10 5-17 11-17s11 7 11 17z" fill="#0a4da6"/><path d="M40 32l9-10 7 6 12-16" fill="none" stroke="#0a4da6" stroke-width="3.5"/><path d="M60 10h9v9" fill="none" stroke="#0a4da6" stroke-width="3.5"/></svg>
    <h3>Personal Growth</h3>
    <p>Track your progress and improve over time.</p>
    <div class="go"><svg width="13" height="13" viewBox="0 0 13 13"><path d="M2 11L11 2M4 2h7v7" fill="none" stroke="#0a4da6" stroke-width="2"/></svg></div>
  </div>
  <div class="feature" style="left:771px">
    <svg class="fi" width="44" height="56" viewBox="0 0 44 56"><path d="M14 4v26l-4-5c-2-2-5-1-5 2l8 14c3 6 7 10 14 10h4c7 0 11-5 11-12V28c0-3-4-3-5-1v-2c0-3-5-3-5 0v-1c0-3-5-3-5 0V4c0-4-8-4-8 0z" fill="#0a4da6"/></svg>
    <h3>Ease of Use</h3>
    <p>Simple, intuitive design for seamless journaling.</p>
    <div class="go"><svg width="13" height="13" viewBox="0 0 13 13"><path d="M2 11L11 2M4 2h7v7" fill="none" stroke="#0a4da6" stroke-width="2"/></svg></div>
  </div>

  <div class="btn btn-soft" style="left:450px;top:474px;width:142px;height:42px">Get Started</div>
  <div class="btn btn-line" style="left:600px;top:474px;width:148px;height:42px;border-color:#9fbbe3">Learn More</div>
</section>

<!-- TESTIMONIALS -->
<div class="abs eyebrow" style="left:0;top:3480px;width:1200px">Hear from Our Users</div>
<h2 class="abs heading" style="left:0;top:3517px;width:1200px">Testimonials From Our<br><span class="accent">Clients.</span></h2>

<div class="abs quote-card">
  <div class="abs quote-photo" role="img" aria-label="Photo of a customer in a dark t-shirt against a soft green background"></div>
  <div class="abs" style="left:470px;top:80px;font-size:26px;letter-spacing:2px;color:var(--blue)">&#9733;&#9733;&#9733;&#9733;&#9733;</div>
  <p class="abs quote-text">Working with Northwind Loop has been transformative for our business. Their expertise in technological consulting, particularly in digital automation, AI, and Big Data, has streamlined our operations and significantly boosted our efficiency.</p>
  <div class="abs" style="left:460px;top:344px;width:460px;height:1px;background:#d6dde7"></div>
  <div class="abs" style="left:460px;top:372px;font-size:15px;font-weight:600;color:var(--ink)">-DARIN OKAFOR</div>
  <div class="abs" style="left:466px;top:394px;font-size:12px;color:var(--text)">Fmr. Co-CEO, Corvant</div>
</div>
<div class="abs next-card" role="img" aria-label="Photo of the next customer testimonial"></div>
<div class="round" style="left:1090px;top:3822px;background:var(--blue-soft)"><svg width="16" height="16" viewBox="0 0 13 13"><path d="M2 11L11 2M4 2h7v7" fill="none" stroke="#0a4da6" stroke-width="1.8"/></svg></div>
<div class="round" style="left:1090px;top:3887px;background:#fff;border:1px solid #d9dde4"><svg width="16" height="16" viewBox="0 0 13 13"><path d="M11 2L2 11M2 4v7h7" fill="none" stroke="#555" stroke-width="1.8"/></svg></div>

<!-- CTA -->
<section class="abs cta">
  <div class="abs eyebrow" style="left:0;top:82px;width:1200px">Ready to Start Reflecting?</div>
  <h2 class="abs heading" style="left:0;top:119px;width:1200px">Join A Community Of Mindful<br>Individuals.</h2>
  <div class="btn btn-soft" style="left:527px;top:233px;width:144px;height:43px">Contact Us</div>
</section>

<!-- FOOTER -->
<footer class="abs footer">
  <div class="abs" style="left:234px;top:64px;font-family:Poppins,sans-serif;font-weight:700;font-size:37px;color:var(--blue)">Moodvane</div>
  <div class="social" style="left:254px" aria-label="Social profile link"></div>
  <div class="social" style="left:299px" aria-label="Social profile link"></div>
  <div class="social" style="left:342px" aria-label="Social profile link"></div>

  <h4 style="left:531px;top:70px">QUICK LINKS</h4>
  <ul style="left:531px;top:96px"><li>Home</li><li>About</li><li>Features</li><li>How It Works</li><li>Contact</li></ul>

  <h4 style="left:757px;top:70px">CONTACT US</h4>
  <div class="contact-line" style="top:98px">
    <svg width="12" height="16" viewBox="0 0 12 16"><path d="M6 1a5 5 0 0 0-5 5c0 4 5 9 5 9s5-5 5-9a5 5 0 0 0-5-5z" fill="none" stroke="#0a4da6" stroke-width="1.6"/><circle cx="6" cy="6" r="1.8" fill="#0a4da6"/></svg>
    <span>Location name will be here near<br>this building 12345 USA</span></div>
  <div class="contact-line" style="top:162px">
    <svg width="13" height="13" viewBox="0 0 13 13"><path d="M3 1l2 3-1.5 1.5c1 2 2 3 4 4L9 8l3 2-1 2C6 12 1 7 1 2z" fill="#0a4da6"/></svg>
    <span>Call us:- <b style="font-weight:500;font-size:12px">0123 555 0199</b></span></div>
  <div class="contact-line" style="top:206px">
    <svg width="13" height="10" viewBox="0 0 13 10"><rect x="0" y="0" width="13" height="10" rx="1" fill="#0a4da6"/><path d="M1 1l5.5 4.5L12 1" fill="none" stroke="#fff"/></svg>
    <span><b style="font-weight:700">Email:-</b><br>hello@moodvane.com</span></div>

  <div class="abs" style="left:234px;top:293px;width:826px;height:1px;background:#dde1e7"></div>
  <div class="copy">Copyright &copy; 2024 <b>Moodvane</b>. All Rights Reserved.</div>
  <div class="abs" style="left:1131px;top:291px;width:38px;height:38px;background:var(--blue);border-radius:3px;display:flex;align-items:center;justify-content:center">
    <svg width="14" height="16" viewBox="0 0 14 16"><path d="M7 15V2M1 8l6-6 6 6" fill="none" stroke="#fff" stroke-width="2"/></svg></div>
</footer>

</body>
</html>
```